Marlow Aviation Group Envelope, Letterhead, Business Card Design

I need designs for a new company letterhead, business cards, and envelopes. These designs will need to be presented using 5 different company logos for the different divisions that are managed under the Marlow Aviation Group umbrella (company names listed below). The member of FRCU logo should also be included.
- Marlow Aviation Group
- Marlow Jet Management
- Marlow Jet Charter
- Marlow Pilot Services
- Marlow Aircraft Sales
- Marlow Flight Training

Logos for the various companies are attached as well as a screen shot of the main page of our website.

```html
<!DOCTYPE html>
<html lang="en">
<head>
<meta charset="utf-8">
<title>Marlow Jet Management – Stationery</title>
<link href="https://fonts.googleapis.com/css2?family=Montserrat:wght@600&family=Roboto:wght@400;500;700&display=swap" rel="stylesheet">
<style>
  :root{
    --blue:#1c5fae;
    --ink:#1a1a1a;
    --grey:#6b6b6b;
    --paper:#ffffff;
    --stage-top:#f4f4f5;
    --stage-mid:#2c2e31;
    --stage-low:#e3e5e7;
  }
  *{margin:0;padding:0;box-sizing:border-box}
  html,body{width:781px;height:1200px;overflow:hidden}
  body{position:relative;font-family:"Roboto",Arial,sans-serif;background:var(--stage-low)}
  .band-top{position:absolute;left:0;top:0;width:781px;height:97px;background:linear-gradient(#f7f7f8,#dcdddf);display:flex;align-items:center;justify-content:center}
  .band-mid{position:absolute;left:0;top:97px;width:781px;height:571px;background:var(--stage-mid)}
  .band-low{position:absolute;left:0;top:668px;width:781px;height:532px;background:linear-gradient(#e9eaec,#dadcdf)}

  .wordmark{font-family:"Montserrat",Arial,sans-serif;font-weight:600;color:var(--blue);text-transform:uppercase;line-height:1}
  .wordmark .line1{display:block;letter-spacing:.06em}
  .wordmark .line2{display:block;letter-spacing:.12em}
  .wordmark.on-blue{color:#fff}
  .band-top .wordmark .line1{font-size:34px}
  .band-top .wordmark .line2{font-size:12.5px;margin-top:5px}

  .sheet{position:absolute;background:var(--paper);box-shadow:0 3px 6px rgba(0,0,0,.25)}
  .stripe{position:absolute;bottom:0;height:4px}
  .stripe.dark{left:0;background:var(--ink)}
  .stripe.blue{right:0;background:var(--blue)}

  /* business card built at 330x190 and scaled */
  .card{position:absolute;width:330px;height:190px;transform-origin:0 0;box-shadow:0 3px 8px rgba(0,0,0,.35)}
  .card-front{background:var(--paper)}
  .card-front .wordmark{position:absolute;left:34px;top:30px}
  .card-front .wordmark .line1{font-size:22px}
  .card-front .wordmark .line2{font-size:8.3px;margin-top:3px;color:var(--blue)}
  .card-front .stripe.dark{width:72px;height:8px}
  .card-front .stripe.blue{width:258px;height:5px}
  .person{position:absolute;right:150px;top:126px;text-align:right}
  .person .name{font-size:12.5px;color:var(--blue);letter-spacing:.02em}
  .person .name b{color:var(--ink);font-weight:700}
  .person .role{font-size:7.5px;color:var(--grey);margin-top:2px}
  .contacts{position:absolute;left:194px;top:106px;list-style:none}
  .contacts li{display:flex;align-items:flex-start;gap:5px;font-size:7.2px;color:var(--grey);line-height:1.25;margin-bottom:6px}
  .contacts li:first-child{margin-bottom:9px}
  .icon{width:9px;height:9px;flex:none;display:block}
  .card-back{background:var(--blue);display:flex;align-items:center;justify-content:center}
  .card-back .wordmark .line1{font-size:25px}
  .card-back .wordmark .line2{font-size:9.6px;margin-top:3px}

  .envelope{left:46px;top:813px;width:342px;height:172px}
  .flap{position:absolute;left:0;top:0;width:342px;height:51px}
  .envelope .wordmark{position:absolute;left:0;right:0;top:15px;text-align:center}
  .envelope .wordmark .line1{font-size:15px}
  .envelope .wordmark .line2{font-size:5.8px;margin-top:2px}

  .slip{left:46px;top:1001px;width:343px;height:182px}
  .slip .wordmark{position:absolute;left:11px;top:15px}
  .slip .wordmark .line1{font-size:15px}
  .slip .wordmark .line2{font-size:5.8px;margin-top:2px}
  .slip .addr{position:absolute;left:11px;top:47px;display:flex;gap:3px;align-items:center;font-size:4.6px;color:var(--grey)}
  .slip .addr .icon{width:5px;height:5px}
  .slip .stripe.dark{width:136px;height:3px}
  .slip .stripe.blue{width:207px;height:3px}

  .letterhead{left:401px;top:704px;width:334px;height:479px}
  .letterhead .wordmark{position:absolute;left:10px;top:18px}
  .letterhead .wordmark .line1{font-size:15px}
  .letterhead .wordmark .line2{font-size:5.8px;margin-top:2px}
  .lh-contacts{position:absolute;right:15px;top:403px;list-style:none;text-align:right}
  .lh-contacts li{display:flex;justify-content:flex-end;align-items:flex-start;gap:3px;font-size:5px;color:var(--grey);line-height:1.25;margin-bottom:4px}
  .lh-contacts li:first-child{margin-bottom:8px}
  .lh-contacts .icon{width:6px;height:6px}
  .letterhead .stripe.dark{width:128px;height:3px}
  .letterhead .stripe.blue{width:206px;height:3px}
</style>
</head>
<body>
<svg width="0" height="0" style="position:absolute" aria-hidden="true">
  <defs>
    <symbol id="i-pin" viewBox="0 0 10 10"><rect width="10" height="10" rx="1" fill="#1a1a1a"/><path d="M5 2a2 2 0 0 1 2 2c0 1.5-2 4-2 4S3 5.5 3 4a2 2 0 0 1 2-2z" fill="#fff"/><circle cx="5" cy="4" r=".8" fill="#1a1a1a"/></symbol>
    <symbol id="i-phone" viewBox="0 0 10 10"><rect width="10" height="10" rx="1" fill="#1c5fae"/><path d="M3 2.2l1.2 1.6-.7.8c.4.9 1 1.5 1.9 1.9l.8-.7 1.6 1.2-.6 1c-2.6-.2-4.6-2.2-4.8-4.8z" fill="#fff"/></symbol>
    <symbol id="i-mail" viewBox="0 0 10 10"><rect width="10" height="10" rx="1" fill="#1c5fae"/><rect x="2" y="3" width="6" height="4" fill="#fff"/><path d="M2 3l3 2.4L8 3" fill="none" stroke="#1c5fae" stroke-width=".7"/></symbol>
    <symbol id="i-web" viewBox="0 0 10 10"><rect width="10" height="10" rx="1" fill="#1c5fae"/><path d="M3 2.5v5l1.4-1.3 1 2 .9-.4-1-2H7.2z" fill="#fff"/></symbol>
  </defs>
</svg>

<header class="band-top">
  <div class="wordmark"><span class="line1">Marlow</span><span class="line2">Jet Management</span></div>
</header>

<section class="band-mid">
  <div class="card card-front" style="left:46px;top:190px">
    <div class="wordmark"><span class="line1">Marlow</span><span class="line2">Jet Management</span></div>
    <div class="person"><div class="name">DANA <b>REYES</b></div><div class="role">Executive Officer</div></div>
    <ul class="contacts">
      <li><svg class="icon"><use href="#i-pin"/></svg><span>48 Hangar Row Ln. Suite 12<br>Dallas, TX 0000</span></li>
      <li><svg class="icon"><use href="#i-phone"/></svg><span>001-555-0142</span></li>
      <li><svg class="icon"><use href="#i-mail"/></svg><span>info@marlowjetsgroup.com</span></li>
      <li><svg class="icon"><use href="#i-web"/></svg><span>marlowjetsgroup.com</span></li>
    </ul>
    <div class="stripe dark"></div><div class="stripe blue"></div>
  </div>
  <div class="card card-back" style="left:405px;top:190px">
    <div class="wordmark on-blue"><span class="line1">Marlow</span><span class="line2">Jet Management</span></div>
  </div>
</section>

<section class="band-low"></section>

<div class="card card-front" style="left:46px;top:704px;transform:scale(.494,.511)">
  <div class="wordmark"><span class="line1">Marlow</span><span class="line2">Jet Management</span></div>
  <div class="person"><div class="name">DANA <b>REYES</b></div><div class="role">Executive Officer</div></div>
  <ul class="contacts">
    <li><svg class="icon"><use href="#i-pin"/></svg><span>48 Hangar Row Ln. Suite 12<br>Dallas, TX 0000</span></li>
    <li><svg class="icon"><use href="#i-phone"/></svg><span>001-555-0142</span></li>
    <li><svg class="icon"><use href="#i-mail"/></svg><span>info@marlowjetsgroup.com</span></li>
    <li><svg class="icon"><use href="#i-web"/></svg><span>marlowjetsgroup.com</span></li>
  </ul>
  <div class="stripe dark"></div><div class="stripe blue"></div>
</div>
<div class="card card-back" style="left:225px;top:704px;transform:scale(.494,.511)">
  <div class="wordmark on-blue"><span class="line1">Marlow</span><span class="line2">Jet Management</span></div>
</div>

<div class="sheet envelope">
  <svg class="flap" viewBox="0 0 342 51" aria-hidden="true"><path d="M0 0H342L328 34Q322 50 306 50H36Q20 50 14 34Z" fill="#1c5fae"/></svg>
  <div class="wordmark on-blue"><span class="line1">Marlow</span><span class="line2">Jet Management</span></div>
</div>

<div class="sheet slip">
  <div class="wordmark"><span class="line1">Marlow</span><span class="line2">Jet Management</span></div>
  <div class="addr"><svg class="icon"><use href="#i-pin"/></svg><span>48 Hangar Row Ln. Suite 12 Dallas, TX 0000</span></div>
  <div class="stripe dark"></div><div class="stripe blue"></div>
</div>

<div class="sheet letterhead">
  <div class="wordmark"><span class="line1">Marlow</span><span class="line2">Jet Management</span></div>
  <ul class="lh-contacts">
    <li><span>48 Hangar Row Ln. Suite 12<br>Dallas, TX 0000</span><svg class="icon"><use href="#i-pin"/></svg></li>
    <li><span>001-555-0142</span><svg class="icon"><use href="#i-phone"/></svg></li>
    <li><span>info@marlowjetsgroup.com</span><svg class="icon"><use href="#i-mail"/></svg></li>
    <li><span>marlowjetsgroup.com</span><svg class="icon"><use href="#i-web"/></svg></li>
  </ul>
  <div class="stripe dark"></div><div class="stripe blue"></div>
</div>
</body>
</html>
```